PTA Meeting Poster

We are looking to create a poster to invite parents of our school to our monthly PTA Meeting.

The copy should include:

PTA Meeting
This Wednesday
8:40am
in the Multi Purpose Room

All Welcome!

```html
<!DOCTYPE html>
<html lang="en">
<head>
<meta charset="UTF-8">
<title>PTA Meeting Poster</title>
<link rel="stylesheet" href="https://fonts.googleapis.com/css2?family=Arimo:wght@400;700&display=swap">
<style>
  :root {
    --page: #ffffff;
    --lime-top: #a6d313;
    --lime-mid: #d6e60a;
    --lime-glow: #eef36a;
    --ink: #1c1a1a;
    --teal: #006f63;
    --accent: #c3e000;
    --crowd-deep: #3a3c4c;
    --crowd-dark: #565a70;
    --crowd-mid: #8c8ea6;
    --crowd-soft: #b9b7c8;
    --floor-light: #f2eeee;
    --floor-warm: #e4d6d4;
  }
  * { margin: 0; padding: 0; box-sizing: border-box; }
  html, body {
    width: 1200px;
    height: 1000px;
    overflow: hidden;
    background: var(--page);
  }
  .poster {
    position: absolute;
    left: 237px;
    top: 20px;
    width: 742px;
    height: 960px;
    background:
      radial-gradient(ellipse 60% 22% at 62% 36%, rgba(255,255,220,0.9), rgba(255,255,220,0) 70%),
      linear-gradient(180deg, var(--lime-top) 0%, var(--lime-mid) 28%, var(--lime-glow) 38%, #f6f8d0 46%, #ffffff 52%);
    font-family: "Arimo", Arial, sans-serif;
    color: var(--ink);
    overflow: hidden;
  }
  .headline,
  .when,
  .where {
    position: absolute;
    line-height: 1;
    white-space: nowrap;
  }
  .headline {
    right: 47px;
    top: 43px;
    font-size: 87px;
    font-weight: 700;
    letter-spacing: 7px;
  }
  .when {
    right: 57px;
    top: 158px;
    font-size: 49px;
    font-weight: 700;
    letter-spacing: 0.6px;
  }
  .where {
    right: 59px;
    top: 213px;
    font-size: 50px;
    font-weight: 400;
    letter-spacing: 0.2px;
  }
  .meeting-photo {
    position: absolute;
    left: 0;
    top: 300px;
    width: 742px;
    height: 540px;
    background:
      radial-gradient(ellipse 22% 30% at 14% 88%, var(--crowd-deep), rgba(58,60,76,0) 75%),
      radial-gradient(ellipse 18% 22% at 30% 70%, var(--floor-light), rgba(242,238,238,0) 70%),
      radial-gradient(ellipse 14% 26% at 46% 40%, var(--crowd-dark), rgba(86,90,112,0) 75%),
      radial-gradient(ellipse 10% 18% at 64% 30%, var(--crowd-dark), rgba(86,90,112,0) 75%),
      radial-gradient(ellipse 18% 30% at 92% 50%, var(--crowd-dark), rgba(86,90,112,0) 75%),
      radial-gradient(ellipse 16% 24% at 90% 88%, var(--crowd-mid), rgba(140,142,166,0) 75%),
      radial-gradient(ellipse 26% 50% at 70% 72%, var(--floor-light), rgba(242,238,238,0) 75%),
      radial-gradient(ellipse 18% 30% at 58% 90%, var(--floor-warm), rgba(228,214,212,0) 75%),
      linear-gradient(100deg, var(--crowd-deep) 0%, var(--crowd-dark) 22%, var(--crowd-mid) 40%, var(--crowd-soft) 52%, var(--floor-light) 66%, var(--crowd-soft) 82%, var(--crowd-mid) 100%);
    -webkit-mask-image: linear-gradient(180deg, transparent 0%, rgba(0,0,0,0.6) 10%, #000 24%);
            mask-image: linear-gradient(180deg, transparent 0%, rgba(0,0,0,0.6) 10%, #000 24%);
  }
  .welcome-band {
    position: absolute;
    left: 0;
    bottom: 0;
    width: 742px;
    height: 120px;
    background: var(--teal);
  }
  .welcome {
    position: absolute;
    right: 56px;
    top: 23px;
    display: flex;
    align-items: flex-end;
    color: var(--accent);
    font-size: 77px;
    font-weight: 700;
    line-height: 1;
    white-space: nowrap;
  }
  .people-icon {
    width: 64px;
    height: 56px;
    margin: 0 36px 9px 2px;
    fill: var(--accent);
  }
</style>
</head>
<body>
  <main class="poster">
    <h1 class="headline">PTA Meeting</h1>
    <p class="when">This Wednesday, 8:40am</p>
    <p class="where">in the Multi Purpose Room</p>

    <div class="meeting-photo" role="img" aria-label="Photo of parents seated in rows at a PTA meeting, listening to two speakers at the front of the room"></div>

    <footer class="welcome-band">
      <p class="welcome">A<svg class="people-icon" viewBox="0 0 62 52" role="img" aria-label="ll">
          <circle cx="15" cy="5" r="5"/>
          <path d="M6 12h18a3 3 0 0 1 3 3v16h-5v21h-4V34h-2v18H12V31H3V15a3 3 0 0 1 3-3z"/>
          <circle cx="45" cy="5" r="5"/>
          <path d="M39 12h12l8 24h-8v16h-4V38h-2v14h-4V36h-8z"/>
        </svg>Welcome!</p>
    </footer>
  </main>
</body>
</html>
```